Ridgeline Build Network Inc. Letterhead

Creation of attractive and eye catching letterhead for a business start-up for the construction industry. Letterhead must relate to construction, but avoid standard hammer and tools in the design.
Updates

I forgot to add some details, sorry about that. Some pertinent info: Ph: 916-555-0148 ridgelinebuildnet.example 487 Willowmere Ave, Ste 210 Folsom, CA 95699 info@ridgelinebuildnet.example not sure if slogan should be in there" “Connecting construction professionals to create a purpose driven industry.” must be able to be used in word. Thanks!

```html
<!DOCTYPE html>
<html lang="en">
<head>
<meta charset="utf-8">
<title>Ridgeline Build Network Inc. Letterhead</title>
<link href="https://fonts.googleapis.com/css2?family=Montserrat:wght@400;500;700&display=swap" rel="stylesheet">
<style>
  :root {
    --brand-red: #c8161d;
    --brand-navy: #1c2260;
    --ink: #2a2a2a;
    --paper: #ffffff;
    --backdrop: #ececec;
  }
  * { margin: 0; padding: 0; box-sizing: border-box; }
  html, body { width: 1200px; height: 800px; overflow: hidden; }
  body {
    background: var(--backdrop);
    font-family: "Montserrat", sans-serif;
    color: var(--ink);
    position: relative;
  }
  .letterhead {
    position: absolute;
    left: 306px; top: 20px;
    width: 588px; height: 760px;
    background: var(--paper);
    box-shadow: 0 2px 10px rgba(0,0,0,0.12);
    overflow: hidden;
  }
  .side-stripe { position: absolute; top: 0; bottom: 0; }
  .side-stripe--red { left: 0; width: 9px; background: var(--brand-red); }
  .side-stripe--navy { left: 14px; width: 7px; background: var(--brand-navy); }
  .company-name {
    position: absolute; left: 52px; top: 52px;
    font-weight: 700; font-size: 14px; line-height: 1.2;
    color: var(--brand-navy);
    display: flex; align-items: center; gap: 8px;
  }
  .company-name .brand-dot {
    width: 10px; height: 10px; border-radius: 50%; background: var(--brand-red);
  }
  .contact-block {
    position: absolute; right: 40px; top: 28px;
    text-align: right; font-size: 8.5px; line-height: 1.45; font-weight: 500;
    color: var(--ink);
  }
  .header-rule {
    position: absolute; left: 52px; right: 40px; top: 92px;
    height: 1px; background: var(--brand-navy);
  }
  .letter-body {
    position: absolute; left: 95px; right: 55px; top: 138px;
    font-size: 9.5px; line-height: 1.5; color: var(--ink);
  }
  .letter-body p { margin-bottom: 11px; text-align: justify; }
  .footer-band { position: absolute; left: 0; bottom: 44px; width: 588px; height: 26px; }
  .footer-url {
    position: absolute; right: 18px; bottom: 50px;
    font-size: 11px; font-weight: 500; color: var(--paper); letter-spacing: 0.3px;
  }
</style>
</head>
<body>
  <main class="letterhead">
    <div class="side-stripe side-stripe--red"></div>
    <div class="side-stripe side-stripe--navy"></div>

    <header>
      <div class="company-name"><span class="brand-dot"></span>Ridgeline Build Network Inc.</div>
      <address class="contact-block" style="font-style:normal">
        Phone: 916-555-0148<br>
        info@ridgelinebuildnet.example<br>
        ridgelinebuildnet.example<br>
        487 Willowmere Ave, Ste 210<br>
        Folsom, CA 95699
      </address>
      <div class="header-rule"></div>
    </header>

    <section class="letter-body">
      <p>Dear :</p>
      <p>Lorem ipsum dolor sit amet, consectetur adipiscing elit. Aenean ut ipsum eget massa hendrerit vestibulum vel in velit. Donec pretium neque velit.</p>
      <p>Aliquam porta lectus nec mauris ornare venenatis. Vivamus non est turpis, et cursus sem. Mauris vehicula erat in diam auctor at bibendum nisl lacinia.</p>
      <p>Morbi imperdiet neque vehicula nunc convallis gravida. Vestibulum iaculis pretium placerat. Integer consequat, est sit amet facilisis eleifend, nibh nibh varius orci, eget dapibus arcu dui non purus. Pellentesque in magna mauris. Duis enim sapien, dictum vitae condimentum a, pulvinar vel lacus. Mauris et molestie nibh. Vestibulum vitae nulla at metus elementum porta sit amet interdum elit. Nulla sollicitudin, eu nulla volutpat congue.</p>
      <p>Velit id dapibus fermentum, turpis sapien ornare dui, ac congue purus. Nunc sed ante dui, in porta lectus. Cras nec habitasse platea dictumst. Maecenas id diam quis dui porta egestas felis. Donec ullamcorper mattis posuere. Phasellus tortor vel dapibus. Vestibulum ante ipsum.</p>
      <p>Velit id dapibus fermentum, turpis sapien ornare dui, ac congue purus. Nunc sed ante dui, in porta lectus. Cras nec habitasse platea dictumst. Maecenas id diam quis dui porta egestas felis. Donec ullamcorper mattis posuere. Phasellus tortor vel dapibus. Vestibulum ante ipsum.</p>
    </section>

    <footer>
      <svg class="footer-band" viewBox="0 0 588 26" aria-hidden="true">
        <polygon points="320,26 332,0 340,0 328,26" fill="var(--brand-navy)"/>
        <polygon points="340,26 352,0 588,0 588,26" fill="var(--brand-red)"/>
      </svg>
      <div class="footer-url">www.ridgelinebuildnet.example</div>
    </footer>
  </main>
</body>
</html>
```